For our product portfolio we need a new packaging design. Our product is a Guaraná-derived energy in powder form. It is sold in small bags, between 350 x 400 mm and 700 x 800 mm, and also in boxes e.g. in the size of 240 x 160 x 45mm.

Our goal is to get creative product design which can be used for
a) the small bags,
b) the boxes, and
c) our Web site logo.

Target Market(s)

Our current target market are computer and Internet geeks. Therefore, we used a LOL-cat in our current/previous design. With the new design we would like to address a broader audience. It would be nice to see logos and packaging designs that are suitable to catch the attention of both geeks as well as normal folks.

Our target audience are people who would buy energy drinks or drink a lot of coffee.

The target audience are young people who work hard and/or go to parties and festivals. The design should be rather playful and funny than serious business.

Industry/Entity Type

Product

Requirements
Must have
• 1. A relationship to the nature product Guaraná. You could, for example, use the red fruits and green leaves of the guarana plant in the design to signal that the product is organic and good for your health. Take a look at http://en.plinthopedia.example/wiki/Guarana for inspirations.
• 2. Our product name is "Velora Fizzpulver"
• 3. The small bags must have certain information in multiple languages (please see image attached as file 1 for reference). We will tell you the specifics when your design is selected as one of our favorites. However, please keep some space in your packaging design for the information text.
• 4. The boxes must have certain information in multiple languages (please see image attached as file 3 for reference). We will tell you the specifics when your design is selected as one of our favorites.
• 5. The graphics must be delivered in an open format so that we can make changes and adjustments after the competition has finished.
• 6. The graphics for packaging must use CMYK colors with at least 600dpi. The logo must use RGB colors with 72dpi.
• Please avoid resemblance with other trademarks, such as Tovimba Borealis.
Nice to have
• A brand identity that is appealing to the "Internet community", e.g. a LOL-cat animal, an Internet meme, or the like.
• Another idea would be to use a hybrid animal, such as http://www.snipmorphs.example/gallery/data/418/medium/stretch_snipmorphs.jpg
• In any case, creative and imaginative submissions are preferred over boring submissions. We are open to all ideas.

```html
<!DOCTYPE html>
<html lang="de">
<head>
<meta charset="utf-8">
<title>Velora Fizzpulver – Verpackung</title>
<link href="https://fonts.googleapis.com/css2?family=Open+Sans:wght@400;600;700;800&display=swap" rel="stylesheet">
<style>
  :root {
    --backdrop: #ecebe7;
    --band: #ffffff;
    --brand-green: #2f8a2a;
    --leaf-green: #7dbb2a;
    --sky-blue: #1f86cf;
    --pale-blue: #bfe0f4;
    --ink: #333333;
    --ink-soft: #555555;
  }
  * { box-sizing: border-box; margin: 0; padding: 0; }
  html, body { width: 1200px; height: 500px; overflow: hidden; }
  body {
    background: var(--backdrop);
    font-family: "Open Sans", Arial, sans-serif;
    color: var(--ink);
    position: relative;
  }
  .presentation-band {
    position: absolute; left: 0; top: 104px; width: 1200px; height: 284px;
    background: var(--band);
  }
  .brand-logo {
    position: absolute; left: 120px; top: 160px; width: 360px; height: 150px;
    display: flex; align-items: center; justify-content: center; gap: 14px;
  }
  .brand-logo__circle {
    width: 34px; height: 34px; border-radius: 50%;
    background: var(--sky-blue); flex: none;
  }
  .brand-logo__name {
    font-weight: 800; font-size: 34px; color: var(--brand-green);
    letter-spacing: 0.5px; white-space: nowrap;
  }
  .pack {
    position: absolute; background: #fff; overflow: hidden;
    box-shadow: 0 3px 10px rgba(0,0,0,0.18);
  }
  .pack__swirl { position: absolute; inset: 0; width: 100%; height: 100%; }
  .pack--front {
    left: 548px; top: 106px; width: 296px; height: 306px;
    transform: rotate(-3deg);
  }
  .pack--front .front-logo {
    position: absolute; left: 58px; top: 104px;
    font-weight: 800; font-size: 21px; color: var(--brand-green);
    white-space: nowrap; transform: rotate(-6deg);
  }
  .pack--front .warning {
    position: absolute; left: 36px; top: 158px; width: 196px;
    font-size: 8px; font-weight: 600; line-height: 1.6;
    color: var(--ink-soft); text-align: center; white-space: nowrap;
    transform: rotate(9deg);
  }
  .pack--back {
    left: 868px; top: 74px; width: 282px; height: 318px;
  }
  .pack--back .claim {
    position: absolute; left: 40px; top: 50px; width: 200px;
    text-align: center; font-size: 9.5px; font-weight: 700; line-height: 1.4;
  }
  .usage-steps {
    position: absolute; left: 52px; top: 100px; display: flex; gap: 14px;
  }
  .usage-step { width: 78px; text-align: center; font-size: 8.5px; white-space: nowrap; }
  .usage-step__picture {
    display: block; width: 48px; height: 56px; margin: 0 auto 8px;
    border-radius: 6px; background: linear-gradient(160deg, #8ecf4a, #2f8a2a);
  }
  .ingredients {
    position: absolute; left: 14px; top: 186px; width: 184px;
    font-size: 8px; line-height: 1.35; text-align: justify;
  }
  .net-amount {
    position: absolute; right: 16px; top: 190px; font-size: 7px; color: var(--ink-soft);
  }
  .recycle-mark {
    position: absolute; left: 206px; top: 182px; width: 10px; height: 10px;
    border: 1.5px solid var(--ink-soft); border-radius: 50%;
  }
  .pack--back .website {
    position: absolute; left: 0; right: 0; bottom: 22px; text-align: center;
    font-size: 8.5px; color: var(--ink-soft);
  }
</style>
</head>
<body>
  <div class="presentation-band"></div>

  <div class="brand-logo">
    <span class="brand-logo__circle"></span>
    <span class="brand-logo__name">Velora Fizzpulver</span>
  </div>

  <section class="pack pack--front">
    <svg class="pack__swirl" viewBox="0 0 296 306" aria-hidden="true">
      <path d="M0 0 H120 C70 40 30 90 0 150 Z" fill="var(--sky-blue)"/>
      <path d="M0 150 C30 90 70 40 120 0 H150 C95 40 45 100 0 180 Z" fill="var(--pale-blue)"/>
      <path d="M0 190 C50 100 110 35 175 0 H185 C115 40 55 110 0 205 Z" fill="var(--sky-blue)"/>
      <path d="M0 60 C25 30 50 10 80 0" stroke="#fff" stroke-width="4" fill="none"/>
      <path d="M0 100 C35 55 70 25 105 0" stroke="#6fb3e6" stroke-width="5" fill="none"/>
      <path d="M296 170 C262 250 190 292 100 306 H296 Z" fill="var(--pale-blue)"/>
      <path d="M296 205 C254 266 196 296 140 306 H296 Z" fill="var(--sky-blue)"/>
      <path d="M296 185 C258 258 188 296 110 306" stroke="var(--leaf-green)" stroke-width="5" fill="none"/>
    </svg>
    <div class="front-logo">Velora Fizzpulver</div>
    <p class="warning">
      Enthält Guarana.<br>
      Erhöhter Koffeingehalt (2,5g Coffein/100g)<br>
      Nicht für Kinder, Schwangere und<br>
      Koffein-empfindliche Personen geeignet
    </p>
  </section>

  <section class="pack pack--back">
    <svg class="pack__swirl" viewBox="0 0 282 318" aria-hidden="true">
      <path d="M60 0 C130 20 200 60 282 140 V0 Z" fill="var(--pale-blue)"/>
      <path d="M130 0 C190 20 240 55 282 95 V0 Z" fill="var(--sky-blue)"/>
      <path d="M20 0 C110 25 200 80 282 175" stroke="var(--leaf-green)" stroke-width="5" fill="none"/>
      <path d="M0 30 C90 40 200 100 282 200" stroke="var(--pale-blue)" stroke-width="3" fill="none"/>
      <path d="M0 270 C100 240 200 250 282 300" stroke="var(--pale-blue)" stroke-width="3" fill="none"/>
    </svg>
    <p class="claim">ist eine belebende<br>energy-scleckbrause auf<br>basic von guarana</p>
    <div class="usage-steps">
      <div class="usage-step">
        <span class="usage-step__picture" role="img" aria-label="Hände reißen die Tüte auf"></span>
        1. aufreissen
      </div>
      <div class="usage-step">
        <span class="usage-step__picture" role="img" aria-label="Pulver wird eingenommen"></span>
        2. einschmeissen
      </div>
    </div>
    <span class="recycle-mark"></span>
    <span class="net-amount">Menge: 5g</span>
    <p class="ingredients">
      Zutaten: Zucker, Guarana Extrakt (Träger: Maltodextrin, Coffein-Menge: 2,5g in 100g Schleckbrause), Säuerungsmittel Citronensäure, Natriumbicarbonat, Maltodextrin, Aromen. Morvenstal &amp; Quade GbR, Lindenhof Allee 9, 40210 Talheim. Mindestens haltbar bis
    </p>
    <p class="website">www.velora-fizzpulver.example</p>
  </section>
</body>
</html>
```